PowerPoint template for my training workshop business

I would like to have a PowerPoint template created using my logo and palette materials created by Brivantelox. I train and facilitate workshops using PowerPoint in both corporate and public settings.

I have attached the original design elements to this request.

```html
<!DOCTYPE html>
<html lang="en">
<head>
<meta charset="utf-8">
<title>Marisol Quenby Coaching – Presentation Template</title>
<link rel="stylesheet" href="https://fonts.googleapis.com/css2?family=Cinzel:wght@700;900&family=Cinzel+Decorative:wght@700;900&family=Open+Sans:ital,wght@0,400;0,600;1,700&display=swap">
<style>
:root{
  --page:#ececec;
  --plum:#68154f;
  --plum-ink:#6d1a52;
  --plum-soft:#7b3466;
  --amber:#f7a11d;
  --gold:#fcc332;
  --lilac:#a4a9c6;
  --teal:#1c3d4d;
  --grey-text:#6f6f6f;
  --band:#dcdce0;
  --white:#ffffff;
}
*{margin:0;padding:0;box-sizing:border-box}
html,body{width:774px;height:1200px;overflow:hidden;background:var(--page)}
body{position:relative;font-family:"Open Sans",Arial,sans-serif}

.slide{position:absolute;width:611px;height:343px;overflow:hidden;background:var(--white);transform:scale(.5025);transform-origin:0 0}
.slide--plum{background:var(--plum)}
.abs{position:absolute}

/* header */
.title-rule{position:absolute;height:1.5px;width:22px;background:var(--amber);top:36px}
.slide-title{position:absolute;left:33px;top:25px;font-family:"Cinzel",serif;font-weight:900;font-size:17px;letter-spacing:2.4px;color:var(--plum-ink);white-space:nowrap}
.brand{position:absolute;display:flex;align-items:center;gap:4px;white-space:nowrap}
.brand-dot{display:block;border-radius:50%;border:2px solid var(--amber)}
.brand-name{font-family:"Cinzel",serif;font-weight:700;color:var(--amber);text-transform:uppercase}
.brand--small{right:33px;top:27px}
.brand--small .brand-dot{width:16px;height:16px}
.brand--small .brand-name{font-size:6.5px;letter-spacing:.3px}
.brand--light .brand-dot{border-color:var(--white)}
.brand--light .brand-name{color:var(--white)}

/* footer */
.footer-band{position:absolute;left:0;right:0;bottom:0;height:16px;background:linear-gradient(90deg,#d4d4da,#ececf0 80%,#e4e4e8)}
.footer-text{position:absolute;left:33px;bottom:5px;font-family:"Cinzel",serif;font-weight:700;font-size:4.6px;letter-spacing:.4px;color:var(--plum-ink)}
.footer-page{position:absolute;right:0;bottom:0;width:41px;height:16px;background:var(--plum);color:var(--amber);font-size:6px;font-weight:600;text-align:center;line-height:16px}
.footer-mark{position:absolute;right:48px;bottom:2px;width:24px;height:24px;border-radius:50%;background:var(--white);border:2px solid var(--amber)}

/* text */
.subtitle{position:absolute;font-family:"Cinzel",serif;font-weight:900;font-size:9.5px;letter-spacing:1.6px;color:var(--amber);white-space:nowrap}
.body{position:absolute;font-size:6px;line-height:8px;letter-spacing:.45px;color:var(--grey-text);text-align:justify}
.body p{margin-bottom:10px}
.lead{position:absolute;left:76px;width:455px;top:88px;font-size:7.6px;line-height:10.3px;letter-spacing:.7px;color:var(--grey-text);text-align:justify}

.photo{position:absolute;background:linear-gradient(135deg,#c9c4bd,#8e8a88 45%,#5c6474 75%,#d7d5d2)}
.photo--warm{background:linear-gradient(135deg,#dcd6cf,#a58a74 40%,#5a4a46 70%,#c9c4c0)}
.photo--cool{background:linear-gradient(135deg,#e0e0e2,#6e7ea1 40%,#3f4760 70%,#c7c9cf)}
</style>
</head>
<body>

<!-- Title slide -->
<section class="slide slide--plum" style="left:234px;top:32px">
  <div class="abs" style="left:25px;top:35px;width:262px;height:262px;border-radius:50%;background:var(--amber)"></div>
  <div class="photo photo--warm" role="img" aria-label="Photo of a coach speaking in a workshop" style="left:43px;top:53px;width:226px;height:226px;border-radius:50%"></div>
  <div class="abs" style="left:582px;top:0;width:1px;height:172px;background:var(--lilac)"></div>
  <div class="brand" style="left:335px;top:92px">
    <span class="brand-dot" style="width:40px;height:40px;border-width:3px"></span>
    <span class="brand-name" style="font-size:13px;letter-spacing:.5px">Marisol Quenby Coaching</span>
  </div>
  <h1 class="abs" style="left:333px;top:152px;font-family:'Cinzel Decorative',serif;font-weight:900;font-size:25px;line-height:23px;letter-spacing:1px;color:var(--amber)">PRESENTATION<br>TITLE</h1>
  <p class="abs" style="left:340px;top:206px;width:240px;font-size:10px;line-height:13.5px;letter-spacing:1px;color:var(--lilac)">Lorem ipsum dolor sit amet, consectetur adipiscing elit, sed do eiusmod tempor incididunt ut</p>
</section>

<!-- Text slide -->
<section class="slide" style="left:70px;top:225px">
  <span class="title-rule" style="left:0"></span><h2 class="slide-title">Slide Title Here</h2><span class="title-rule" style="left:243px"></span>
  <div class="brand brand--small"><span class="brand-dot"></span><span class="brand-name">Marisol Quenby Coaching</span></div>
  <h3 class="subtitle" style="left:33px;top:63px">Subtitle Goes Here</h3>
  <div class="body" style="left:33px;top:86px;width:545px">
    <p>Lorem ipsum dolor sit amet, consectetur adipiscing elit, sed do eiusmod tempor incididunt ut labore et dolore magna aliqua. Ut enim ad minim veniam, quis nostrud exercitation ullamco laboris nisi ut aliquip ex ea commodo consequat. Duis aute irure dolor in reprehenderit in voluptate velit esse cillum dolore eu fugiat nulla pariatur.</p>
    <p>Excepteur sint occaecat cupidatat non proident, sunt in culpa qui officia deserunt mollit anim id est laborum. Sed ut perspiciatis unde omnis iste natus error sit voluptatem accusantium doloremque laudantium, totam rem aperiam, eaque ipsa quae ab illo inventore veritatis et quasi architecto beatae vitae dicta sunt explicabo. Nemo enim ipsam voluptatem quia voluptas sit aspernatur aut odit aut fugit, sed quia consequuntur magni dolores eos qui ratione voluptatem sequi nesciunt.</p>
    <p>Lorem ipsum dolor sit amet, consectetur adipiscing elit, sed do eiusmod tempor incididunt ut labore et dolore magna aliqua. Ut enim ad minim veniam, quis nostrud exercitation ullamco laboris nisi ut aliquip ex ea commodo consequat. Duis aute irure dolor in reprehenderit in voluptate velit esse cillum dolore eu fugiat nulla pariatur. Excepteur sint occaecat cupidatat non proident, sunt in culpa qui officia deserunt mollit anim id est laborum. Sed ut perspiciatis unde omnis iste natus error sit voluptatem accusantium doloremque laudantium, totam rem aperiam, eaque ipsa quae ab illo inventore veritatis et quasi architecto beatae vitae dicta sunt explicabo. Nemo enim ipsam voluptatem quia voluptas sit aspernatur aut odit aut fugit, sed quia consequuntur magni dolores eos qui ratione voluptatem sequi nesciunt.</p>
    <p>Inventore veritatis et quasi architecto beatae vitae dicta sunt explicabo. Nemo enim ipsam voluptatem quia voluptas sit aspernatur aut odit aut fugit, sed quia consequuntur magni dolores eos qui ratione voluptatem sequi nesciunt. Neque porro quisquam est, qui dolorem ipsum quia dolor sit amet, consectetur.</p>
  </div>
  <div class="footer-band"></div><span class="footer-text">COPYRIGHT © 2020 | MARISOL QUENBY COACHING</span><span class="footer-mark"></span><span class="footer-page">1</span>
</section>

<!-- Text and photo slide -->
<section class="slide" style="left:397px;top:225px">
  <svg class="abs" style="left:0;top:0" width="611" height="343" viewBox="0 0 611 343">
    <path d="M410,0 C335,80 318,250 425,327 L611,327 L611,0 Z" fill="#f7a11d"/>
  </svg>
  <svg class="abs" style="left:0;top:0" width="611" height="343" viewBox="0 0 611 343" role="img" aria-label="Photo of a workshop participant at a laptop">
    <defs><linearGradient id="photoCool" x1="0" y1="0" x2="1" y2="1"><stop offset="0" stop-color="#e0e0e2"/><stop offset=".45" stop-color="#6e7ea1"/><stop offset=".75" stop-color="#3f4760"/><stop offset="1" stop-color="#c7c9cf"/></linearGradient></defs>
    <path d="M432,0 C362,80 352,250 446,327 L611,327 L611,0 Z" fill="url(#photoCool)"/>
  </svg>
  <span class="title-rule" style="left:0"></span><h2 class="slide-title">Slide Title Here</h2><span class="title-rule" style="left:243px"></span>
  <div class="brand brand--small"><span class="brand-dot"></span><span class="brand-name">Marisol Quenby Coaching</span></div>
  <h3 class="subtitle" style="left:33px;top:63px">Subtitle Goes Here</h3>
  <div class="body" style="left:33px;top:86px;width:258px">
    <p>Lorem ipsum dolor sit amet, consectetur adipiscing elit, sed do eiusmod tempor incididunt ut labore et dolore magna aliqua. Ut enim ad minim veniam, quis nostrud exercitation ullamco laboris nisi ut aliquip ex ea commodo consequat. Duis aute irure dolor in reprehenderit in voluptate velit esse cillum dolore eu fugiat nulla pariatur.</p>
    <p>Excepteur sint occaecat cupidatat non proident, sunt in culpa qui officia deserunt mollit anim id est laborum. Sed ut perspiciatis unde omnis iste natus error sit voluptatem accusantium doloremque laudantium, totam rem aperiam, eaque ipsa quae ab illo inventore veritatis et quasi architecto beatae vitae dicta sunt explicabo. Nemo enim ipsam voluptatem quia voluptas sit aspernatur aut odit aut fugit, sed quia consequuntur magni dolores eos qui ratione voluptatem sequi nesciunt.</p>
    <p>Lorem ipsum dolor sit amet, consectetur adipiscing elit, sed do eiusmod tempor incididunt ut labore et dolore magna aliqua. Ut enim ad minim veniam, quis nostrud exercitation ullamco laboris nisi ut aliquip ex ea commodo consequat.</p>
  </div>
  <div class="footer-band"></div><span class="footer-text">COPYRIGHT © 2020 | MARISOL QUENBY COACHING</span><span class="footer-mark"></span><span class="footer-page">1</span>
</section>

<!-- Three column slide -->
<section class="slide" style="left:70px;top:418px">
  <span class="title-rule" style="left:0"></span><h2 class="slide-title">Slide Title Here</h2><span class="title-rule" style="left:243px"></span>
  <div class="brand brand--small"><span class="brand-dot"></span><span class="brand-name">Marisol Quenby Coaching</span></div>
  <div class="body" style="left:33px;top:82px;width:545px">
    <p>Lorem ipsum dolor sit amet, consectetur adipiscing elit, sed do eiusmod tempor incididunt ut labore et dolore magna aliqua. Ut enim ad minim veniam, quis nostrud exercitation ullamco laboris nisi ut aliquip ex ea commodo consequat. Duis aute irure dolor in reprehenderit in voluptate velit esse cillum dolore eu fugiat nulla pariatur.</p>
    <p>Excepteur sint occaecat cupidatat non proident, sunt in culpa qui officia deserunt mollit anim id est laborum. Sed ut perspiciatis unde omnis iste natus error sit voluptatem accusantium doloremque laudantium, totam rem aperiam, eaque ipsa quae ab illo inventore veritatis et quasi architecto beatae vitae dicta sunt explicabo. Nemo enim ipsam voluptatem quia voluptas sit aspernatur aut odit aut fugit, sed quia consequuntur magni dolores eos qui ratione voluptatem sequi nesciunt.</p>
  </div>
  <h3 class="subtitle" style="left:33px;top:199px">Subtitle Goes Here</h3>
  <h3 class="subtitle" style="left:221px;top:199px;color:var(--teal)">Subtitle Goes Here</h3>
  <span class="abs" style="left:221px;top:221px;width:22px;height:1.5px;background:var(--teal)"></span>
  <h3 class="subtitle" style="left:409px;top:199px;color:var(--plum-ink)">Subtitle Goes Here</h3>
  <span class="abs" style="left:409px;top:221px;width:22px;height:1.5px;background:var(--plum-ink)"></span>
  <p class="body" style="left:33px;top:230px;width:170px">Lorem ipsum dolor sit amet, consectetur adipiscing elit, sed do eiusmod tempor incididunt ut labore et dolore magna aliqua. Ut enim ad minim veniam, quis nostrud exercitation ullamco laboris nisi ut aliquip ex ea commodo consequat.</p>
  <p class="body" style="left:221px;top:230px;width:170px">Lorem ipsum dolor sit amet, consectetur adipiscing elit, sed do eiusmod tempor incididunt ut labore et dolore magna aliqua. Ut enim ad minim veniam, quis nostrud exercitation ullamco laboris nisi ut aliquip ex ea commodo consequat.</p>
  <p class="body" style="left:409px;top:230px;width:170px">Lorem ipsum dolor sit amet, consectetur adipiscing elit, sed do eiusmod tempor incididunt ut labore et dolore magna aliqua. Ut enim ad minim veniam, quis nostrud exercitation ullamco laboris nisi ut aliquip ex ea commodo consequat.</p>
  <div class="footer-band"></div><span class="footer-text">COPYRIGHT © 2020 | MARISOL QUENBY COACHING</span><span class="footer-mark"></span><span class="footer-page">1</span>
</section>

<!-- List slide -->
<section class="slide" style="left:397px;top:418px">
  <span class="title-rule" style="left:0"></span><h2 class="slide-title">Slide Title Here</h2><span class="title-rule" style="left:243px"></span>
  <div class="brand brand--small"><span class="brand-dot"></span><span class="brand-name">Marisol Quenby Coaching</span></div>
  <p class="lead">Excepteur sint occaecat cupidatat non proident, sunt in culpa qui officia deserunt mollit anim id est laborum. Sed ut perspiciatis unde omnis iste natus error sit voluptatem accusantium doloremque laudantium, totam rem aperiam, eaque ipsa quae ab illo inventore veritatis et quasi architecto beatae vitae dicta sunt explicabo. Nemo enim ipsam voluptatem quia voluptas sit aspernatur ut est, qui dolam quaerat voluptatem.</p>
  <ol class="abs" style="left:230px;top:163px;list-style:none;font-size:8px;letter-spacing:.6px;color:var(--grey-text)">
    <li style="height:28px"><b style="font-family:Cinzel,serif;color:var(--amber);display:inline-block;width:14px">1</b>Lorem ipsum dolor sit amet</li>
    <li style="height:28px"><b style="font-family:Cinzel,serif;color:var(--plum-ink);display:inline-block;width:14px">2</b>Lorem ipsum dolor sit amet</li>
    <li style="height:28px"><b style="font-family:Cinzel,serif;color:var(--amber);display:inline-block;width:14px">3</b>Lorem ipsum dolor sit amet</li>
    <li style="height:28px"><b style="font-family:Cinzel,serif;color:var(--plum-ink);display:inline-block;width:14px">4</b>Lorem ipsum dolor sit amet</li>
    <li style="height:28px"><b style="font-family:Cinzel,serif;color:var(--amber);display:inline-block;width:14px">5</b>Lorem ipsum dolor sit amet</li>
  </ol>
  <div class="footer-band"></div><span class="footer-text">COPYRIGHT © 2020 | MARISOL QUENBY COACHING</span><span class="footer-mark"></span><span class="footer-page">1</span>
</section>

<!-- Section break -->
<section class="slide" style="left:70px;top:610px">
  <div class="photo" role="img" aria-label="Workshop group photo tinted in plum" style="left:0;top:0;width:611px;height:343px;background:linear-gradient(120deg,#6b2a5a,#7b3466 45%,#84406f 60%,#6a2858)"></div>
  <span class="abs" style="left:172px;top:171px;width:24px;height:1.5px;background:var(--amber)"></span>
  <h2 class="abs" style="left:0;width:611px;top:160px;text-align:center;font-family:Cinzel,serif;font-weight:900;font-size:17px;letter-spacing:2.4px;color:var(--white)">SECTION BREAK</h2>
  <span class="abs" style="left:415px;top:171px;width:24px;height:1.5px;background:var(--amber)"></span>
  <p class="abs" style="left:75px;width:461px;top:210px;text-align:center;font-size:8px;line-height:10.3px;letter-spacing:.7px;color:var(--white)">Excepteur sint occaecat cupidatat non proident, sunt in culpa qui officia deserunt mollit anim id est laborum. Sed ut perspiciatis unde omnis iste natus error sit voluptatem accusantium doloremque laudantium, totam rem aperiam, eaque</p>
</section>

<!-- Two photo slide -->
<section class="slide" style="left:397px;top:610px">
  <span class="title-rule" style="left:0"></span><h2 class="slide-title">Slide Title Here</h2><span class="title-rule" style="left:243px"></span>
  <div class="brand brand--small"><span class="brand-dot"></span><span class="brand-name">Marisol Quenby Coaching</span></div>
  <p class="lead">Excepteur sint occaecat cupidatat non proident, sunt in culpa qui officia deserunt mollit anim id est laborum. Sed ut perspiciatis unde omnis iste natus error sit voluptatem accusantium doloremque laudantium, totam rem aperiam, eaque ipsa quae ab illo inventore veritatis et quasi architecto beatae vitae dicta sunt explicabo. Nemo enim ipsam voluptatem quia voluptas sit aspernatur ut est, qui dolam quaerat voluptatem.</p>
  <div class="abs" style="left:0;top:220px;width:611px;height:107px;background:linear-gradient(180deg,var(--gold),var(--amber))"></div>
  <div class="photo photo--warm" role="img" aria-label="Photo of a coach presenting" style="left:76px;top:162px;width:219px;height:126px"></div>
  <div class="photo photo--cool" role="img" aria-label="Photo of a participant listening" style="left:307px;top:162px;width:219px;height:126px"></div>
  <div class="footer-band"></div><span class="footer-text">COPYRIGHT © 2020 | MARISOL QUENBY COACHING</span><span class="footer-mark"></span><span class="footer-page">1</span>
</section>

<!-- My story slide -->
<section class="slide" style="left:70px;top:803px">
  <svg class="abs" style="left:0;top:0" width="611" height="343" viewBox="0 0 611 343">
    <defs><linearGradient id="storyBand" x1="0" y1="0" x2="1" y2="0"><stop offset="0" stop-color="#f7a11d"/><stop offset="1" stop-color="#fcc332"/></linearGradient></defs>
    <path d="M0,0 H611 V62 Q305,150 0,62 Z" fill="url(#storyBand)"/>
  </svg>
  <span class="title-rule" style="left:0;background:var(--plum-ink)"></span>
  <h2 class="slide-title" style="left:35px">My Story</h2>
  <span class="title-rule" style="left:156px;background:var(--plum-ink)"></span>
  <div class="brand brand--small brand--light"><span class="brand-dot"></span><span class="brand-name">Marisol Quenby Coaching</span></div>
  <div class="photo photo--warm" role="img" aria-label="Portrait photo of the coach" style="left:251px;top:44px;width:107px;height:107px;border-radius:50%;border:2px solid #8a8a8a"></div>
  <h3 class="subtitle" style="left:0;width:611px;text-align:center;top:163px;color:var(--plum-ink)">Subtitle Goes Here</h3>
  <p class="abs" style="left:66px;top:202px;width:231px;font-size:7.6px;line-height:10.2px;letter-spacing:.6px;color:var(--grey-text);text-align:justify">Excepteur sint occaecat cupidatat non proident, sunt in culpa qui officia deserunt mollit anim id est laborum. Sed ut perspiciatis unde omnis iste natus error sit voluptatem accusantium doloremque laudantium, totam rem aperiam, eaque ipsa quae ab illo inventore veritatis et quasi architecto beatae vitae dicta sunt explicabo. Nemo enim ipsam voluptatem quia voluptas sit aspernatur ut est, qui dolam quaerat voluptatem.</p>
  <p class="abs" style="left:314px;top:202px;width:231px;font-size:7.6px;line-height:10.2px;letter-spacing:.6px;color:var(--grey-text);text-align:justify">Excepteur sint occaecat cupidatat non proident, sunt in culpa qui officia deserunt mollit anim id est laborum. Sed ut perspiciatis unde omnis iste natus error sit voluptatem accusantium doloremque laudantium, totam rem aperiam, eaque ipsa quae ab illo inventore veritatis et quasi architecto beatae vitae dicta sunt explicabo. Nemo enim ipsam voluptatem quia voluptas sit aspernatur ut est, qui dolam quaerat voluptatem.</p>
  <div class="footer-band"></div><span class="footer-text">COPYRIGHT © 2020 | MARISOL QUENBY COACHING</span><span class="footer-mark"></span><span class="footer-page">1</span>
</section>

<!-- Quote slide -->
<section class="slide" style="left:397px;top:803px">
  <span class="title-rule" style="left:0"></span><h2 class="slide-title">Slide Title Here</h2><span class="title-rule" style="left:243px"></span>
  <div class="brand brand--small"><span class="brand-dot"></span><span class="brand-name">Marisol Quenby Coaching</span></div>
  <blockquote class="abs" style="left:57px;top:64px;width:235px;font-style:italic;font-weight:700;font-size:15px;line-height:20.2px;letter-spacing:1px;color:var(--amber)">“Lorem ipsum dolor sit amet, consectetur adipisicing elit, sed do eiusmod tempor incidi­dunt ut labore et dolore magna aliqua. Ut enim ad minim veniam, quis nostrud exercitation ullamco laboris nisi commodo consequat.”</blockquote>
  <span class="abs" style="left:72px;top:309px;width:23px;height:1.5px;background:var(--amber)"></span>
  <p class="abs" style="left:105px;top:300px;font-family:Cinzel,serif;font-weight:900;font-size:13px;letter-spacing:1.8px;color:var(--plum-ink)">JOHN DOE</p>
  <div class="abs" style="left:336px;top:92px;width:204px;height:204px;border-radius:50%;background:var(--amber)"></div>
  <div class="photo photo--warm" role="img" aria-label="Photo of a coaching conversation" style="left:315px;top:66px;width:192px;height:192px;border-radius:50%"></div>
  <div class="footer-band"></div><span class="footer-text">COPYRIGHT © 2020 | MARISOL QUENBY COACHING</span><span class="footer-mark"></span><span class="footer-page">1</span>
</section>

<!-- Closing slide -->
<section class="slide slide--plum" style="left:234px;top:996px">
  <div class="abs" style="left:540px;top:0;width:1px;height:160px;background:var(--lilac)"></div>
  <h2 class="abs" style="left:200px;width:340px;top:150px;text-align:center;font-family:'Cinzel Decorative',serif;font-weight:900;font-size:30px;letter-spacing:1px;color:var(--amber)">THANK YOU</h2>
  <div class="brand" style="left:277px;top:215px">
    <span class="brand-dot" style="width:42px;height:42px;border-width:3px"></span>
    <span class="brand-name" style="font-size:13px;letter-spacing:.5px">Marisol Quenby Coaching</span>
  </div>
</section>

</body>
</html>
```